Ashcombe Heritage Guild Harvest Lantern Days Event Flyer - Historic Event

I need a flyer about the Ashcombe Heritage Guild's Harvest Lantern Days event October 8th and 9th. The centerpiece of Harvest Lantern Days is Civil War reenactments. I want the flyer to include the schedule of events and be eye catching on area bulletin boards. Our website is www.ashcombeheritageguild.org for more information and pictures. The website for the Calder Ridge Rangers reenactors is http://www.calderridgerangers.com/.

Target Market(s)

Our target market is middle ages (35-70) families and couples. Most are history buffs, especially about the Civil War.

Industry/Entity Type

Non-Profit

Font styles to use
Serif
Decorative
Script

Requirements
Must have
• The flyer must include the majority of the schedule attached - especially the battle times, museums, and anything including food.The dance on Saturday night is also important. The bottom of the flyer MUST say "Paid in part by Quillan County Visitor Levy Board"
Nice to have
• Pictures

```html
<!DOCTYPE html>
<html lang="en">
<head>
<meta charset="utf-8">
<title>Ashcombe Heritage Guild – Harvest Lantern Days</title>
<link rel="stylesheet" href="https://fonts.googleapis.com/css2?family=Cinzel:wght@400;700;900&family=Roboto+Condensed:wght@400;700&display=swap">
<style>
  :root {
    --bg: #3a2416;
    --bg-deep: #2a190e;
    --orange: #e27a22;
    --gold: #c89a46;
    --gold-pale: #e0c486;
    --cream: #efe6d6;
    --white: #ffffff;
    --sepia-a: #c9b08a;
    --sepia-b: #6e5436;
    --forest-a: #6f7a4a;
    --forest-b: #3d3a22;
  }
  * { margin: 0; padding: 0; box-sizing: border-box; }
  html, body { width: 849px; height: 1200px; overflow: hidden; background: var(--bg-deep); }
  .flyer {
    position: relative; width: 849px; height: 1200px; overflow: hidden;
    background: radial-gradient(ellipse at 30% 60%, #4a2f1c 0%, var(--bg) 55%, var(--bg-deep) 100%);
    font-family: "Roboto Condensed", Arial, sans-serif; color: var(--white);
  }
  .bands { position: absolute; inset: 0; }
  .photo { position: absolute; }
  .photo-portrait {
    left: 0; top: 0; width: 340px; height: 215px;
    clip-path: polygon(0 0, 100% 0, 62% 100%, 0 100%);
    background: linear-gradient(135deg, var(--sepia-a), var(--sepia-b));
  }
  .photo-camp {
    left: 330px; top: 265px; width: 200px; height: 160px;
    clip-path: polygon(30% 0, 100% 0, 70% 100%, 0 100%);
    background: linear-gradient(160deg, #8a7a5a, #4b3a25);
  }
  .photo-reenactors {
    left: 470px; top: 300px; width: 379px; height: 560px;
    clip-path: polygon(38% 0, 100% 0, 100% 100%, 0 100%, 0 55%);
    background: linear-gradient(170deg, var(--forest-a) 0%, #58603a 45%, var(--forest-b) 100%);
  }
  .photo-cabin {
    left: 525px; top: 835px; width: 225px; height: 170px;
    background: linear-gradient(160deg, #9a8c6e, #5a4630);
    border: 3px solid var(--gold);
  }
  .header { position: absolute; right: 24px; top: 28px; text-align: right; }
  .header-dates { font-family: "Cinzel", Georgia, serif; font-weight: 900; color: var(--orange); font-size: 46px; line-height: 1; }
  .header-dates sup { font-size: 24px; }
  .header-host { font-family: "Cinzel", Georgia, serif; font-weight: 700; font-size: 17px; margin-top: 18px; letter-spacing: .5px; }
  .header-phone { font-family: "Cinzel", Georgia, serif; font-weight: 700; font-size: 21px; margin-top: 10px; }
  .header-email { font-size: 14px; margin-top: 14px; }
  .title { position: absolute; left: 58px; top: 205px; font-family: "Cinzel", Georgia, serif; color: var(--cream); text-shadow: 0 2px 6px rgba(0,0,0,.6); }
  .title-name { font-size: 54px; line-height: 1; letter-spacing: 1px; }
  .title-guild { font-size: 21px; font-weight: 700; margin-top: 10px; letter-spacing: 1px; }
  .title-event { font-size: 46px; font-weight: 900; line-height: 1.05; margin-top: 4px; color: var(--gold-pale); }
  .schedule { position: absolute; left: 40px; top: 470px; width: 420px; font-size: 13.5px; line-height: 1.42; }
  .day { font-weight: 700; color: var(--orange); font-size: 15px; margin-bottom: 2px; }
  .schedule p { color: var(--cream); }
  .schedule .day-sunday { margin-top: 16px; }
  .footer { position: absolute; left: 0; right: 0; top: 1048px; text-align: center; }
  .footer-credit { font-family: "Cinzel", Georgia, serif; font-weight: 700; color: var(--orange); font-size: 25px; }
  .footer-web { font-family: "Cinzel", Georgia, serif; font-size: 17px; margin-top: 18px; letter-spacing: .5px; }
</style>
</head>
<body>
<div class="flyer">
  <svg class="bands" width="849" height="1200" viewBox="0 0 849 1200" aria-hidden="true">
    <polygon points="470,0 520,0 150,860 100,860" fill="#c89a46" opacity=".55"/>
    <polygon points="540,0 560,0 190,860 170,860" fill="#c89a46" opacity=".35"/>
    <polygon points="300,250 849,250 849,270 290,270" fill="#c89a46" opacity=".5"/>
    <polygon points="0,1030 849,1030 849,1036 0,1036" fill="#c89a46"/>
  </svg>

  <div class="photo photo-portrait" role="img" aria-label="Sepia portrait of a family from the 1800s"></div>
  <div class="photo photo-camp" role="img" aria-label="Reenactors gathered at a period camp"></div>
  <div class="photo photo-reenactors" role="img" aria-label="Civil War reenactors and musicians performing outdoors"></div>
  <div class="photo photo-cabin" role="img" aria-label="Small wooden log cabin"></div>

  <header class="header">
    <div class="header-dates">OCTOBER 8<sup>th</sup>–9<sup>th</sup></div>
    <div class="header-host">ASHCOMBE HERITAGE GUILD’S</div>
    <div class="header-phone">(555)614-2870</div>
    <div class="header-email">AshcombeHeritageGuild@mailbox.org</div>
  </header>

  <h1 class="title">
    <div class="title-name">ASHCOMBE</div>
    <div class="title-guild">HERITAGE GUILD’S</div>
    <div class="title-event">HARVEST LANTERN DAYS</div>
  </h1>

  <section class="schedule">
    <div class="day">SATURDAY, OCTOBER 8TH, 2016</div>
    <p>Throughout the Day – Demonstrations and Speakers in various locations</p>
    <p>10:00 AM – Battle by Calder Ridge Rangers</p>
    <p>Sponsored in part by Harlan’s General Stores</p>
    <p>11:30-1:00 – Chicken Biscuit Bake at Town Hall – Free Will Donation</p>
    <p>Afternoon – Trolley and Buggy Rides</p>
    <p>1:00-4:00 Museums Open</p>
    <p>1:30-2:00 Birthday Cake on Merritt House Front Porch</p>
    <p>Cake donated by Greenway Market – Ridgefield</p>
    <p>2:00 Battle by Calder Ridge Rangers</p>
    <p>3:00 Sightseeing Cruise on the Spirit of Ashcombe</p>
    <p>6:00-? Dance at Town Hall with Lockwood Band</p>
    <p>Sponsored by Dr. Pell</p>
    <div class="day day-sunday">SUNDAY, OCTOBER 9TH, 2016</div>
    <p>12:30 PM Parade on Main Street</p>
    <p>Afternoon – Buggy &amp; Trolley Rides</p>
    <p>1:00-4:00 Museums Open</p>
    <p>1:30 Battle by Calder Ridge Rangers</p>
    <p>2:00 Pie Reception at Ashcombe Depot and Railroad History Museum</p>
    <p>3:00 Sightseeing Cruise</p>
  </section>

  <footer class="footer">
    <div class="footer-credit">Paid in part by Quillan County Visitor Levy Board</div>
    <div class="footer-web">www.ashcombeheritageguild.org</div>
  </footer>
</div>
</body>
</html>
```